Window and GutterCleaning Flyer A5 size double sided.

We need a double sided A5 flyer. Side 1, is for window cleaning, side 2 is for gutter cleaning. Licensed by Borough of Calderwick Authority.
Phone number 0800 471 3926.
Business address 17 Fenmarrow Loan, West Brankholm Edinburgh EH47 3TP.
www.bright-pane-services.example
We use a LoftOrb Gutter inspection Cam to view your gutters first to see if they need doing.
Window cleaning ; Professional window cleaning services, what we offer, water fed pole window cleaning able to reach windows up to 60 feet.
Conservatory cleaning.
Conservatory roof cleaning.
Fascias & Soffits cleaning.
Excellent Customer Service.
Target Market(s)
domestic houses
Industry/Entity Type
window cleaning
Look and feel
Each slider illustrates characteristics of the customer's brand and the style your logo design should communicate.

```html
<!DOCTYPE html>
<html lang="en">
<head>
<meta charset="utf-8">
<title>Bright Pane Services – Window &amp; Gutter Cleaning Flyer</title>
<link rel="stylesheet" href="https://fonts.googleapis.com/css2?family=Poppins:wght@400;500;600;700;800&display=swap">
<style>
  :root{
    --stage:#6e6e6e;
    --navy:#28295f;
    --navy-deep:#1f2152;
    --sky:#7db3e6;
    --pale:#a8cdf1;
    --arrow:#1f4f8f;
    --ink:#1b1b1b;
    --white:#ffffff;
    --gold:#c9a23a;
    --photo-brick:#a7705a;
    --photo-glass:#cfdde6;
  }
  *{margin:0;padding:0;box-sizing:border-box}
  html,body{width:1200px;height:841px;overflow:hidden}
  body{background:var(--stage);font-family:"Poppins",sans-serif;color:var(--ink);position:relative}
  .flyer{position:absolute;top:60px;height:736px;background:var(--white);overflow:hidden;box-shadow:0 2px 6px rgba(0,0,0,.35)}
  .flyer--window{left:64px;width:519px}
  .flyer--gutter{left:609px;width:525px}
  .abs{position:absolute}
  .photo{position:absolute}

  /* ---- window side ---- */
  .hero-photo{left:0;top:0;width:519px;height:270px;background:linear-gradient(180deg,#e9eef2 0%,var(--photo-glass) 45%,var(--photo-brick) 100%)}
  .hero-curve{left:0;top:200px}
  .side-column{left:318px;top:197px;width:201px;height:477px;background:var(--navy);border-radius:0 0 0 26px}
  .roof-ring{left:316px;top:150px;width:206px;height:206px;border-radius:50%;background:var(--pale)}
  .roof-photo{left:325px;top:159px;width:188px;height:188px;border-radius:50%;background:linear-gradient(135deg,#8b8a62 0%,#c8ccc8 55%,#e8eaea 100%)}
  .guarantee-badge{left:224px;top:232px;width:92px;height:92px;border-radius:50%;background:radial-gradient(circle,#f4e2a0 0%,var(--gold) 70%,#8d6d1e 100%)}
  .tag-pill{left:0;top:246px;width:139px;height:23px;background:var(--navy);border-radius:0 12px 12px 0;color:var(--white);font-size:14px;font-weight:500;line-height:23px;padding-left:20px;letter-spacing:.2px}
  .headline{font-weight:700;line-height:.95;letter-spacing:.5px}
  .headline .light{color:var(--sky);display:block}
  .headline .dark{color:var(--navy);display:block}
  .window-title{left:15px;top:278px;font-size:39px}
  .body-copy{font-size:12.6px;line-height:14.8px;color:var(--ink)}
  .window-copy{left:19px;top:357px;width:280px;text-align:justify}
  .why-pill{left:17px;top:490px;width:135px;height:24px;background:var(--navy);border-radius:12px;color:var(--white);font-weight:700;font-size:16px;letter-spacing:3px;line-height:24px;padding-left:23px}
  .benefit{left:142px;width:230px;display:flex;gap:7px}
  .benefit svg{flex:none}
  .benefit h4{font-size:12.5px;font-weight:700;color:var(--navy);line-height:14px;margin-top:2px}
  .benefit p{font-size:12.5px;color:#2b2b5c;line-height:14px}
  .brand-mark{display:flex;flex-direction:column;align-items:center;gap:6px;width:108px;text-align:center}
  .brand-mark .square{width:44px;height:44px;background:var(--navy)}
  .brand-mark .name{font-size:14px;font-weight:700;color:var(--navy);line-height:16px}
  .conserv-title{left:331px;top:398px;font-size:19px;font-weight:700;color:var(--sky);line-height:24px}
  .conserv-copy{left:331px;top:423px;width:182px;color:var(--white);font-size:12.2px;line-height:14.8px}
  .conserv-photo{left:331px;top:536px;width:177px;height:138px;background:linear-gradient(180deg,#b6c3cf 0%,#8a6a58 55%,#6f7a5e 100%)}
  .footer-band{left:0;top:660px}
  .phone{font-size:19px;font-weight:700;color:var(--navy);line-height:22px}
  .address{font-size:13px;color:var(--navy-deep);line-height:15px}
  .web{font-size:12px;font-weight:700;color:var(--navy);letter-spacing:.4px}

  /* ---- gutter side ---- */
  .gutter-photo{left:250px;top:0;width:275px;height:235px;background:linear-gradient(160deg,#7f8b6a 0%,#c9c9c4 45%,#e9e9e6 70%,#a45a4a 100%)}
  .gutter-swoosh{left:0;top:150px}
  .gutter-blob{left:0;top:0;width:276px;height:264px;background:var(--navy);border-radius:0 0 150px 0 / 0 0 140px 0}
  .gutter-title{left:17px;top:16px}
  .gutter-title .light{font-size:46px}
  .gutter-title .white{color:var(--white);display:block;font-size:34px}
  .gutter-copy{left:21px;top:107px;width:214px;color:var(--white);font-size:12.4px;line-height:14.7px}
  .camera-card{left:245px;top:229px;width:261px;height:221px;border:2px solid #8fa6c8;border-radius:16px;background:var(--pale);padding:11px 0 0 24px}
  .camera-card h3{font-size:19px;font-weight:700;color:var(--navy);line-height:22px}
  .camera-card p{font-size:12.3px;line-height:13.6px;color:var(--navy-deep);width:225px;margin-top:2px}
  .camera-photo{left:4px;top:91px;width:250px;height:122px;background:linear-gradient(90deg,#7e9a5c 0%,#b9c6a8 40%,#4d4d4d 60%,#2e2e2e 100%)}
  .fascia-title{left:17px;top:283px;font-size:40px;line-height:34px}
  .fascia-copy{left:19px;top:398px;width:212px;font-size:12.2px;line-height:14.8px}
  .soffit-photo{left:219px;top:463px;width:306px;height:196px;clip-path:polygon(66% 0,100% 0,100% 100%,0 100%);background:linear-gradient(200deg,#2c2c2c 0%,#f1f1f1 30%,#e2e2e2 60%,#9a5a44 100%)}
  .part-arrow{color:var(--white);font-size:13px;font-weight:600}
  .more-pill{left:292px;top:678px;width:214px;height:24px;background:var(--navy);border-radius:12px;color:var(--white);font-size:14.5px;font-weight:500;text-align:center;line-height:24px}
</style>
</head>
<body>

<!-- ================= SIDE 1: WINDOW CLEANING ================= -->
<section class="flyer flyer--window">
  <div class="photo hero-photo" role="img" aria-label="Photo of a white uPVC conservatory with glass roof against a brick house"></div>
  <svg class="abs hero-curve" width="519" height="120" viewBox="0 0 519 120" aria-hidden="true">
    <path d="M0 78 C80 20 200 28 300 72 L519 72 L519 120 L0 120 Z" fill="var(--pale)"/>
    <path d="M0 86 C80 30 200 38 300 80 L519 80 L519 120 L0 120 Z" fill="var(--white)"/>
  </svg>
  <div class="abs side-column"></div>
  <div class="abs roof-ring"></div>
  <div class="photo roof-photo" role="img" aria-label="Close-up photo of a dirty conservatory roof panel being cleaned"></div>
  <div class="abs guarantee-badge" role="img" aria-label="Satisfaction guarantee seal"></div>

  <div class="abs tag-pill">PROFESSIONAL</div>
  <h1 class="abs headline window-title"><span class="light">WINDOW</span><span class="dark">CLEANING</span></h1>
  <p class="abs body-copy window-copy">Regular domestic or commercial window cleaning helps to avoid the build-up of dirt and residue on the glass, meaning more light can get into your home or business. It can also improve the external appearance of your property. We have water fed pole window cleaning able to reach windows up to 60 feet.</p>

  <div class="abs why-pill">WHY US</div>
  <div class="abs benefit" style="top:487px">
    <svg width="30" height="30" viewBox="0 0 30 30" aria-hidden="true"><circle cx="15" cy="15" r="13" fill="var(--pale)"/><path d="M8 15 l5 6 L25 4" stroke="var(--navy)" stroke-width="4" fill="none" stroke-linecap="round"/></svg>
    <div><h4>COMPETITIVE</h4><p>Fair Pricing &amp;<br>Free Estimates</p></div>
  </div>
  <div class="abs benefit" style="top:543px">
    <svg width="30" height="30" viewBox="0 0 30 30" aria-hidden="true"><circle cx="15" cy="15" r="13" fill="var(--pale)"/><path d="M8 15 l5 6 L25 4" stroke="var(--navy)" stroke-width="4" fill="none" stroke-linecap="round"/></svg>
    <div><h4>EXPERIENCED</h4><p>Over 30 years<br>experience</p></div>
  </div>
  <div class="abs benefit" style="top:597px">
    <svg width="30" height="30" viewBox="0 0 30 30" aria-hidden="true"><circle cx="15" cy="15" r="13" fill="var(--pale)"/><path d="M8 15 l5 6 L25 4" stroke="var(--navy)" stroke-width="4" fill="none" stroke-linecap="round"/></svg>
    <div><h4>LICENSED<br>&amp; REGULATED</h4><p>by Borough of<br>Calderwick Authority</p></div>
  </div>

  <div class="abs brand-mark" style="left:19px;top:566px">
    <span class="square"></span>
    <span class="name">Bright Pane Services</span>
  </div>

  <h2 class="abs conserv-title">CONSERVATORIES</h2>
  <p class="abs conserv-copy">Conservatories &amp; sunrooms take a lot of punishment from the elements. We'll help you get them cleaned up, improving their appearance &amp; getting more light back into the room.</p>
  <div class="photo conserv-photo" role="img" aria-label="Photo of a window cleaner with a water fed pole cleaning a conservatory"></div>

  <svg class="abs footer-band" width="519" height="76" viewBox="0 0 519 76" aria-hidden="true">
    <path d="M0 0 L250 0 C285 0 290 40 330 58 C345 66 360 66 380 66 L519 66 L519 76 L0 76 Z" fill="var(--pale)"/>
  </svg>
  <div class="abs" style="left:21px;top:675px">
    <div class="phone">0800 471 3926</div>
    <div class="address">17 Fenmarrow Loan, West Brankholm<br>Edinburgh EH47 3TP.</div>
  </div>
  <div class="abs web" style="left:290px;top:707px">BRIGHT-PANE-SERVICES.EXAMPLE</div>
</section>

<!-- ================= SIDE 2: GUTTER CLEANING ================= -->
<section class="flyer flyer--gutter">
  <div class="photo gutter-photo" role="img" aria-label="Photo of a vacuum hose clearing moss from a white gutter"></div>
  <svg class="abs gutter-swoosh" width="525" height="140" viewBox="0 0 525 140" aria-hidden="true">
    <path d="M200 110 C300 40 420 60 525 100 L525 140 L200 140 Z" fill="var(--pale)"/>
    <path d="M200 118 C300 52 420 72 525 112 L525 140 L200 140 Z" fill="var(--white)"/>
  </svg>
  <div class="abs gutter-blob"></div>
  <h1 class="abs headline gutter-title"><span class="light">GUTTER</span><span class="white">CLEANING</span></h1>
  <p class="abs gutter-copy">Gutters are an important part of your home. Letting your gutters bget blocked up can cause damage to your property, so why not set up an annual plan and make sure you don't run into problems when winter comes.</p>

  <div class="abs camera-card">
    <h3>LOFTORB CAMERA</h3>
    <p>We use a LoftOrb Gutter inspection Cam to view your gutters first to see if they need doing.</p>
    <div class="photo camera-photo" role="img" aria-label="Photo of a pole-mounted gutter camera beside its monitor screen"></div>
  </div>

  <h1 class="abs headline fascia-title"><span class="light">FASCIA</span><span class="light">&amp; SOFFIT</span><span class="dark">CLEANING</span></h1>
  <p class="abs body-copy fascia-copy">A thorough fascia wash involves the exterior cleaning of UPVC gutters, fascia, soffits (cladding) and exterior of downpipes. This can make a huge difference to the look of your home. We use a range of safe chemicals and, for the majority of cleans, they are non-abrasive so will not damage or scratch the plastics.</p>

  <div class="photo soffit-photo" role="img" aria-label="Photo of a clean white gutter, fascia board and soffit on a brick house"></div>
  <svg class="abs" style="left:228px;top:478px" width="180" height="160" viewBox="0 0 180 160" aria-hidden="true">
    <path d="M68 4 L150 4 L150 0 L172 21 L150 42 L150 37 L68 37 L76 20 Z" fill="var(--arrow)"/>
    <path d="M38 58 L118 58 L118 54 L140 75 L118 96 L118 91 L38 91 L46 74 Z" fill="var(--arrow)"/>
    <path d="M4 116 L86 116 L86 112 L108 133 L86 154 L86 149 L4 149 L12 132 Z" fill="var(--arrow)"/>
  </svg>
  <span class="abs part-arrow" style="left:323px;top:490px">Gutter</span>
  <span class="abs part-arrow" style="left:290px;top:544px">Fascia</span>
  <span class="abs part-arrow" style="left:252px;top:602px">Soffit</span>

  <div class="abs brand-mark" style="left:20px;top:566px">
    <span class="square"></span>
    <span class="name">Bright Pane Services</span>
  </div>

  <svg class="abs" style="left:0;top:660px" width="525" height="76" viewBox="0 0 525 76" aria-hidden="true">
    <path d="M0 0 L230 0 C262 0 268 40 305 58 C320 66 335 66 355 66 L525 66 L525 76 L0 76 Z" fill="var(--pale)"/>
  </svg>
  <div class="abs" style="left:19px;top:675px">
    <div class="phone">0800 471 3926</div>
    <div class="address">17 Fenmarrow Loan, West Brankholm<br>Edinburgh EH47 3TP.</div>
  </div>
  <div class="abs more-pill">FOR MORE INFORMATION</div>
  <div class="abs web" style="left:292px;top:707px">BRIGHT-PANE-SERVICES.EXAMPLE</div>
</section>

</body>
</html>
```